Logo & Responsive Website Design for Mortgage Company

Vantor Mortgage is a new Mortgage Fin-Tech company that will use its own innovative, proprietary technology for lead generation, mortgage origination, and processing of residential home loans in the US. The design should convey that we are a technology-driven company, offering borrowers seeking home loans an exceptional experience throughout the borrowing process.

We are looking for designs that are elegant, convey technical competency, simple to navigate, and set us apart from the competition.

We are not set on any particular colors at this point, so feel free to choose the best colors for your particular designs.

Please include both desktop and mobile designs.

Some Examples of Mortgage Websites. These are to show the typical content, not designs that we particularly like or dislike.
https://www.plumvane.com/
https://www.qbtfunding.com/
https://dorvelmortgage.com/
https://kelvo.com/
https://corvabaylending.com/

Please send comments with additional questions.

Thank You For your participation.

Target Market(s)

U.S. Residential Home Loan Seekers

Industry/Entity Type

FinTech Mortgage

Number of Pages Required

2 page

```html
<!DOCTYPE html>
<html lang="en">
<head>
<meta charset="utf-8">
<title>Vantor Mortgage</title>
<link href="https://fonts.googleapis.com/css2?family=Montserrat:wght@400;500;600;700&display=swap" rel="stylesheet">
<style>
:root{
  --green:#17c264;
  --green-dark:#0fa553;
  --ink:#111111;
  --text:#1c1c1c;
  --muted:#7a7a7a;
  --line:#e3e3e3;
  --field:#f1f1f1;
  --soft:#f3f3f3;
  --white:#ffffff;
  --teal-a:#3fcf9a;
  --teal-b:#7fdcc0;
}
*{box-sizing:border-box;margin:0;padding:0}
html,body{width:1200px;height:5273px;overflow:hidden}
body{font-family:'Montserrat',sans-serif;color:var(--text);background:var(--white);position:relative}
.section{position:absolute;left:0;width:1200px}
.abs{position:absolute}
.eyebrow{color:var(--green);font-size:14px;font-weight:500}
.h2{font-size:33px;font-weight:700;line-height:1.15;color:var(--ink)}
.btn{display:inline-flex;align-items:center;justify-content:center;background:var(--green);color:#fff;font-size:13px;font-weight:500;border-radius:4px}
.photo{position:absolute}

/* header / hero */
.hero{top:0;height:670px;background:var(--ink)}
.hero-photo{left:86px;top:98px;width:879px;height:572px;background:linear-gradient(120deg,#3a3d40,#6d6a64 45%,#8a8680 70%,#4a4c4e)}
.hero-shade{left:86px;top:98px;width:600px;height:572px;background:linear-gradient(90deg,rgba(0,0,0,.55),rgba(0,0,0,0))}
.brand{left:84px;top:18px;color:#fff;font-size:25px;font-weight:700;line-height:1.35}
.nav{left:314px;top:40px;display:flex;gap:30px;color:#fff;font-size:13px}
.phone{left:814px;top:40px;color:#fff;font-size:13px;display:flex;gap:10px;align-items:center}
.nav-cta{left:978px;top:28px;width:135px;height:44px;gap:8px}
.hero-eyebrow{left:135px;top:224px;color:var(--green);font-size:14px}
.hero-title{left:134px;top:258px;color:#fff;font-size:60px;font-weight:700;line-height:1.15}
.hero-btns{left:135px;top:492px;display:flex;gap:22px}
.hero-btns span{height:44px;padding:0 24px;border-radius:4px;display:flex;align-items:center;font-size:13px}
.b-green{background:var(--green);color:#fff}
.b-white{background:#fff;color:var(--ink)}
.calc{left:614px;top:158px;width:501px;height:450px;background:#fff;border-radius:6px;padding:36px 36px}
.calc h3{color:var(--green);font-size:18px;font-weight:600;margin-bottom:26px}
.calc .field{height:46px;background:var(--field);border:1px solid var(--line);border-radius:4px;margin-bottom:22px;display:flex;align-items:center;justify-content:space-between;padding:0 16px;font-size:13px;color:var(--muted)}
.spin{width:14px;height:22px;border:1px solid #ccc;border-radius:2px;background:#fafafa}
.calc .btn{width:100%;height:46px;font-size:14px}

/* about */
.about{top:670px;height:700px}
.about .eyebrow{position:absolute;left:84px;top:170px}
.about .h2{position:absolute;left:84px;top:204px;width:420px}
.about p{position:absolute;left:84px;top:334px;width:460px;font-size:13px;line-height:1.6;color:var(--muted)}
.ticks{position:absolute;left:84px;top:432px;list-style:none;font-size:13px;color:var(--text)}
.ticks li{margin-bottom:18px;display:flex;gap:10px}
.ticks li::before{content:"»";color:var(--green)}
.about-a{left:632px;top:130px;width:271px;height:442px;background:linear-gradient(160deg,#d9d2c8,#8d6d58 60%,#e8e2d9)}
.about-b{left:929px;top:130px;width:271px;height:442px;background:linear-gradient(160deg,#3f5d86,#c9a46a 55%,#e0d3c0)}

/* quote */
.quote{top:1372px;height:283px}
.quote-card{left:0;top:0;width:598px;height:283px;background:#fff;box-shadow:0 2px 14px rgba(0,0,0,.08)}
.quote .h2{position:absolute;left:86px;top:56px;font-size:31px}
.quote p{position:absolute;left:86px;top:110px;width:450px;font-size:13px;line-height:1.6;color:var(--muted)}
.quote .btn{position:absolute;left:86px;top:174px;width:146px;height:44px}
.quote-photo{left:598px;top:0;width:602px;height:283px;background:linear-gradient(150deg,#dfe8df,#c7bba5 40%,#6d8e5c 75%,#a9b19a)}

/* offer */
.offer{top:1655px;height:770px}
.center{position:absolute;left:0;width:1200px;text-align:center}
.offer .eyebrow{top:124px}
.offer .h2{top:154px}
.card{position:absolute;top:217px;width:325px;height:420px;background:#fff;box-shadow:0 2px 14px rgba(0,0,0,.08)}
.card .img{height:245px}
.card .icon{position:absolute;left:36px;top:218px;width:54px;height:54px;border-radius:50%;background:var(--green);border:4px solid #fff;display:flex;align-items:center;justify-content:center}
.card h4{position:absolute;left:33px;top:290px;width:260px;font-size:17px;font-weight:600;line-height:1.45;color:var(--ink)}
.card .more{position:absolute;left:33px;top:370px;color:var(--green);font-size:13px}
.card.active{border-bottom:5px solid var(--green)}

/* faq */
.faq{top:2424px;height:756px;background:var(--soft)}
.faq .eyebrow{position:absolute;left:84px;top:128px}
.faq .h2{position:absolute;left:86px;top:160px}
.acc{position:absolute;left:86px;width:480px;background:#fff;border:1px solid var(--line);padding:0 24px}
.acc h5{font-size:14px;font-weight:600;display:flex;justify-content:space-between;align-items:center;height:54px;color:var(--ink)}
.acc p{font-size:13px;line-height:1.6;color:var(--muted);padding-bottom:22px;margin-top:-6px}
.dot{width:20px;height:20px;border-radius:50%;background:var(--green);color:#fff;font-size:16px;line-height:20px;text-align:center;font-weight:700}
.faq-blob{left:640px;top:160px;width:475px;height:442px}

/* testimonials */
.testi{top:3180px;height:708px}
.testi .eyebrow{top:128px}
.testi .h2{top:160px}
.tcard{position:absolute;top:281px;width:325px;height:300px;border:1px solid var(--line);background:#fff;padding:54px 30px 0}
.tcard.dark{background:var(--ink);border-color:var(--ink);color:#fff}
.avatar{position:absolute;left:30px;top:-40px;width:72px;height:72px;border-radius:50%;background:#fff;border:1px solid var(--line);display:flex;align-items:center;justify-content:center}
.tcard.dark .avatar{background:var(--green);border-color:var(--green)}
.stars{color:#f2b600;font-size:20px;letter-spacing:2px}
.tcard h6{font-size:16px;font-weight:600;margin-top:12px}
.tcard .loc{font-size:12px;color:var(--green);margin-top:4px}
.tcard p{font-size:13px;line-height:1.65;color:var(--muted);margin-top:24px}
.tcard.dark p{color:#ddd}

/* contact */
.contact{top:3888px;height:682px;background:var(--ink)}
.contact .eyebrow{position:absolute;left:84px;top:128px}
.contact .h2{position:absolute;left:86px;top:160px;color:#fff}
.in{position:absolute;height:46px;background:var(--field);border-radius:3px;font-size:13px;color:#999;padding:14px 16px}
.contact .btn{position:absolute;left:86px;top:508px;width:146px;height:44px}
.contact-photo{left:676px;top:0;width:524px;height:682px;background:linear-gradient(160deg,#f1f2f3,#d7dde2 45%,#6a7686 80%,#c9cdd2)}

/* newsletter */
.news{top:4570px;height:200px;background:linear-gradient(90deg,var(--teal-a),var(--teal-b))}
.news h3{position:absolute;left:86px;top:68px;color:#fff;font-size:33px;font-weight:700;line-height:1.15}
.sub{position:absolute;left:614px;top:72px;width:500px;height:54px;background:#fff;border-radius:4px;padding:0 6px 0 22px;display:flex;align-items:center;justify-content:space-between;font-size:13px;color:#999}
.sub .btn{width:110px;height:44px}

/* footer */
.footer{top:4770px;height:503px}
.f-brand{left:84px;top:120px;font-size:27px;font-weight:700;line-height:1.3;color:var(--ink)}
.f-about{left:86px;top:200px;width:300px;font-size:13px;line-height:1.6;color:var(--muted)}
.socials{left:86px;top:278px;display:flex;gap:12px}
.socials span{width:34px;height:34px;border-radius:50%;border:1px solid var(--line);display:flex;align-items:center;justify-content:center}
.socials span::after{content:"";width:10px;height:10px;border-radius:50%;background:var(--ink)}
.fcol{position:absolute;top:122px}
.fcol h6{font-size:17px;font-weight:600;color:var(--ink);padding-bottom:12px;position:relative}
.fcol h6::after{content:"";position:absolute;left:0;bottom:0;width:40px;height:2px;background:var(--green)}
.fcol ul{list-style:none;margin-top:26px;font-size:13px;color:var(--muted)}
.fcol li{margin-bottom:30px;display:flex;gap:12px;align-items:center}
.fcol li::before{content:"";width:7px;height:7px;background:var(--green)}
.addr .row{display:flex;gap:14px;font-size:13px;line-height:1.6;color:var(--muted);margin-bottom:20px}
.footer .rule{position:absolute;left:86px;top:410px;width:1029px;height:1px;background:var(--line)}
.copy{position:absolute;left:0;width:1200px;top:440px;text-align:center;font-size:13px;color:var(--ink)}
</style>
</head>
<body>

<section class="section hero">
  <div class="photo hero-photo" role="img" aria-label="Couple meeting a mortgage advisor at a desk"></div>
  <div class="photo hero-shade"></div>
  <div class="abs brand">Vantor<br>Mortgage</div>
  <nav class="abs nav"><span>Know Your Options</span><span>About Us</span><span>Reviews</span><span>Contact Us</span></nav>
  <div class="abs phone">
    <svg width="14" height="14" viewBox="0 0 24 24"><path fill="#17c264" d="M6.6 10.8a15 15 0 0 0 6.6 6.6l2.2-2.2a1 1 0 0 1 1-.25 11.4 11.4 0 0 0 3.6.57 1 1 0 0 1 1 1V20a1 1 0 0 1-1 1A17 17 0 0 1 3 4a1 1 0 0 1 1-1h3.5a1 1 0 0 1 1 1c0 1.25.2 2.45.57 3.6a1 1 0 0 1-.25 1z"/></svg>
    (+01) 482 903 17
  </div>
  <div class="abs btn nav-cta">
    <svg width="14" height="14" viewBox="0 0 24 24" fill="none" stroke="#fff" stroke-width="2"><path d="M18 13v6a2 2 0 0 1-2 2H5a2 2 0 0 1-2-2V8a2 2 0 0 1 2-2h6M15 3h6v6M10 14 21 3"/></svg>
    Calculator
  </div>
  <div class="abs hero-eyebrow">Welcome to Vantor Mortgage</div>
  <h1 class="abs hero-title">Mortgage Is<br>A Great For<br>You</h1>
  <div class="abs hero-btns"><span class="b-green">I'm purchasing</span><span class="b-white">I'm refinancing</span></div>
  <div class="abs calc">
    <h3>Mortgage Calculator</h3>
    <div class="field">Total Amount (30,000$)<span class="spin"></span></div>
    <div class="field">Down Payment (6,000$)<span class="spin"></span></div>
    <div class="field">Interest Rate (4%)<span class="spin"></span></div>
    <div class="field">Mortgage Period (30)<span class="spin"></span></div>
    <div class="btn">Calculate</div>
  </div>
</section>

<section class="section about">
  <div class="eyebrow">About Our Company</div>
  <h2 class="h2">Vantor Mortgage is a new Mortgage Fin-Tech company</h2>
  <p>Vantor Mortgage is a new Mortgage Fin-Tech company that will use its own innovative, proprietary technology for lead generation, mortgage origination, and processing of residential home loans in the US.</p>
  <ul class="ticks">
    <li>Phasellus blandit porta lacus quis pellentesque.</li>
    <li>Phasellus in tempus mauris, nec mattis diam.</li>
    <li>Cras faucibus sodales nunc</li>
  </ul>
  <div class="photo about-a" role="img" aria-label="Woman holding a small model house"></div>
  <div class="photo about-b" role="img" aria-label="Clients shaking hands with an advisor"></div>
</section>

<section class="section quote">
  <div class="photo quote-card"></div>
  <h2 class="h2">Get Mortgage Quote</h2>
  <p>Lorem ipsum dolor sit amet, consectetur adipisicing elitsed do eiusmod tempor incididunt</p>
  <div class="btn">Get A Quote</div>
  <div class="photo quote-photo" role="img" aria-label="Family standing in front of their new house"></div>
</section>

<section class="section offer">
  <div class="center eyebrow">Why Choose Us</div>
  <h2 class="center h2">We Have Offer To You</h2>
  <div class="card active" style="left:86px">
    <div class="img" role="img" aria-label="Laptop showing lead generation charts" style="background:linear-gradient(150deg,#5a4a3c,#c9c2b5 55%,#7a6a58)"></div>
    <div class="icon"><svg width="22" height="22" viewBox="0 0 24 24" fill="#fff"><circle cx="12" cy="6" r="3"/><path d="M6 12h12v3H6zM10 16h4v6h-4z"/></svg></div>
    <h4>Innovative, proprietary technology for lead generation</h4>
    <div class="more">Read More →</div>
  </div>
  <div class="card" style="left:438px">
    <div class="img" role="img" aria-label="Couple using a laptop at home" style="background:linear-gradient(150deg,#e7e1d6,#b79b7e 55%,#d9d3c8)"></div>
    <div class="icon"><svg width="22" height="22" viewBox="0 0 24 24" fill="#fff"><rect x="5" y="3" width="12" height="16" rx="1"/><rect x="8" y="7" width="12" height="14" rx="1" fill="#0fa553"/></svg></div>
    <h4>Innovative, proprietary technology for mortgage origination</h4>
    <div class="more">Read More →</div>
  </div>
  <div class="card" style="left:790px">
    <div class="img" role="img" aria-label="Hands holding a model house and keys" style="background:linear-gradient(150deg,#f2efea,#d8cfc3 55%,#e9a86a)"></div>
    <div class="icon"><svg width="22" height="22" viewBox="0 0 24 24" fill="none" stroke="#fff" stroke-width="2"><path d="M3 11 12 4l9 7M6 9v11h12V9"/></svg></div>
    <h4>Processing of residential home loans in the US</h4>
    <div class="more">Read More →</div>
  </div>
</section>

<section class="section faq">
  <div class="eyebrow">Frequently Asked Questions</div>
  <h2 class="h2">Need Help?We're always<br>here to guide you</h2>
  <div class="acc" style="top:262px">
    <h5>How Do You Qualify For A Loan?<span class="dot">−</span></h5>
    <p>Donec sollicitudin molestie malesuada. Vivamus magna justo, lacinia eget consectetur sed, convallis at tellus. Quisque velit nisi, pretium ut lacinia in</p>
  </div>
  <div class="acc" style="top:424px"><h5>A Good Lender Will Clearly Explain Mortgage?<span class="dot">+</span></h5></div>
  <div class="acc" style="top:494px"><h5>How Much Home Can You Afford?<span class="dot">+</span></h5></div>
  <div class="acc" style="top:568px"><h5>What does a mortgage Advisor do?<span class="dot">+</span></h5></div>
  <svg class="abs faq-blob" viewBox="0 0 475 442" role="img" aria-label="Model houses resting on banknotes">
    <defs><linearGradient id="blobFill" x1="0" y1="0" x2="1" y2="1"><stop offset="0" stop-color="#2c2c2c"/><stop offset=".5" stop-color="#8a8a86"/><stop offset="1" stop-color="#d6d4cf"/></linearGradient></defs>
    <path fill="url(#blobFill)" d="M150 20C250-20 420 10 465 140 495 230 420 330 320 360 220 390 130 470 60 400 0 340 10 260 30 180 45 110 70 50 150 20Z"/>
  </svg>
</section>

<section class="section testi">
  <div class="center eyebrow">Testimonials</div>
  <h2 class="center h2">People Are Saying About Us</h2>
  <div class="tcard" style="left:86px">
    <div class="avatar"><svg width="26" height="26" viewBox="0 0 24 24" fill="#111"><circle cx="12" cy="7" r="5"/><path d="M3 22a9 9 0 0 1 18 0z"/></svg></div>
    <div class="stars">☆☆☆☆☆</div><h6>Marla Westbrook</h6><div class="loc">United States</div>
    <p>Phasellus blandit porta lacus quis pellentesque. Phasellus in tempus mauris, nec mattis diam. Cras faucibus sodales nunc, at faucibus risus convallis quis.</p>
  </div>
  <div class="tcard dark" style="left:438px">
    <div class="avatar"><svg width="26" height="26" viewBox="0 0 24 24" fill="#fff"><circle cx="12" cy="7" r="5"/><path d="M3 22a9 9 0 0 1 18 0z"/></svg></div>
    <div class="stars">☆☆☆☆☆</div><h6>Marla Westbrook</h6><div class="loc">United States</div>
    <p>Phasellus blandit porta lacus quis pellentesque. Phasellus in tempus mauris, nec mattis diam. Cras faucibus sodales nunc, at faucibus risus convallis quis.</p>
  </div>
  <div class="tcard" style="left:790px">
    <div class="avatar"><svg width="26" height="26" viewBox="0 0 24 24" fill="#111"><circle cx="12" cy="7" r="5"/><path d="M3 22a9 9 0 0 1 18 0z"/></svg></div>
    <div class="stars">☆☆☆☆☆</div><h6>Marla Westbrook</h6><div class="loc">United States</div>
    <p>Phasellus blandit porta lacus quis pellentesque. Phasellus in tempus mauris, nec mattis diam. Cras faucibus sodales nunc, at faucibus risus convallis quis.</p>
  </div>
</section>

<section class="section contact">
  <div class="eyebrow">Let's Contact</div>
  <h2 class="h2">Contact With Us</h2>
  <div class="in" style="left:86px;top:242px;width:240px">Name</div>
  <div class="in" style="left:342px;top:242px;width:240px">Email</div>
  <div class="in" style="left:86px;top:310px;width:240px">Phone</div>
  <div class="in" style="left:342px;top:310px;width:240px">Subject</div>
  <div class="in" style="left:86px;top:386px;width:496px;height:108px">Your message</div>
  <div class="btn">Send Message</div>
  <div class="photo contact-photo" role="img" aria-label="Smiling advisor holding a small model house"></div>
</section>

<section class="section news">
  <h3>Do You Want to Get Update<br>What's Upcoming?</h3>
  <div class="sub">Enter your email<span class="btn">Subscribe</span></div>
</section>

<footer class="section footer">
  <div class="abs f-brand">Vantor<br>Mortgage</div>
  <div class="abs f-about">Lorem ipsum dolor sit amet, consectetur adipisicing elitsed do eiusmod tempor incididunt ut labore et dolore</div>
  <div class="abs socials"><span></span><span></span><span></span></div>
  <div class="fcol" style="left:438px"><h6>Quick Links</h6><ul><li>Know Your Options</li><li>About Us</li><li>Reviews</li><li>Contact Us</li></ul></div>
  <div class="fcol" style="left:667px"><h6>Support</h6><ul><li>Contact</li><li>Our Blog</li><li>Privacy Policy</li><li>Terms &amp; Conditions</li></ul></div>
  <div class="fcol addr" style="left:906px">
    <h6>Address</h6>
    <div style="margin-top:26px">
      <div class="row"><svg width="14" height="16" viewBox="0 0 24 24" fill="#17c264"><path d="M12 2a7 7 0 0 0-7 7c0 5 7 13 7 13s7-8 7-13a7 7 0 0 0-7-7zm0 9.5A2.5 2.5 0 1 1 12 6a2.5 2.5 0 0 1 0 5.5z"/></svg><span>Enter your location here<br>Lorem ipsum</span></div>
      <div class="row"><svg width="14" height="16" viewBox="0 0 24 24" fill="#17c264"><path d="M6.6 10.8a15 15 0 0 0 6.6 6.6l2.2-2.2a1 1 0 0 1 1-.25 11.4 11.4 0 0 0 3.6.57 1 1 0 0 1 1 1V20a1 1 0 0 1-1 1A17 17 0 0 1 3 4a1 1 0 0 1 1-1h3.5a1 1 0 0 1 1 1c0 1.25.2 2.45.57 3.6a1 1 0 0 1-.25 1z"/></svg><span>Phone:<br>(+01) 482 903 17</span></div>
      <div class="row"><svg width="14" height="16" viewBox="0 0 24 24" fill="#17c264"><path d="M2 5h20v14H2zm2 2v.5l8 5 8-5V7z"/></svg><span>Email:<br>info@vantor-mail.com</span></div>
    </div>
  </div>
  <div class="rule"></div>
  <div class="copy">Copyright ©2022 Vantor Mortgage</div>
</footer>

</body>
</html>
```